Professional "Aviation Parts" Auction Website with Customer Login Backend Module

Need an "Aviation Parts" Website with 4 major listing options.
- AUCTION
Seller can list their items on the site as an auction with a small listing fee. Seller has to create an account in order to be able to create or edit a listing. Seller must be able to have a reserve price.
- SELLING
Sellers can list their items with a small listing fee. Imortant is, that Sellers has a back end module, (like trovix) where they can log in and create or make changes to existing listings.
- BUYING
Buyers can search items either by part number in a search bar, or scroll through categories and subcategories to find the respective part.
- WANTED
Customers should be able to create a “Wanted” listing for items of interest.

In all four cases, customers (Buyers/Seller) must create an account to either place a bid, buy now, create a “wanted” listing or create/edit their own for sale/auction listing. NO login is required to search the website or browse through categories and to see listings. The website should be “Trovix like” with login module, payment, coindrop connection, etc and easy to navigate. A design example is https://www.quellmarket-hub.com/ . I’m open for all ideas.

Target Market(s)

Aviation Industry
Helicopter Industry

Industry/Entity Type

Aviation

Number of Pages Required

5+ page

Font styles to use
Serif
Sans Serif

Colors
85acd3
3176b5
9d9d9d
d3d3d3

Requirements
Must have
• Our company is called Brelvox.com, LLC and is specialized in aviation parts listings. The website must have 4 major options: Auction, Sell, Buy, and Wanted listings. The Buyer/Seller must create an account in order to bid, buy or sell an item. No login is required if someone just wants to browse the website to look for pricing and parts. Once they decide to purchase, they have to login or create an account. The same counts for the seller. Seller must create an account to list a "For Sale", "Auction" or "Wanted" Listing. Each listing requires a small listing fee, which will be charged by us and should be paid via CoinDrop. CoinDrop should be interfaced as a preferred payment method. Other payment options are available as well. The website idea is very similar to Trovix. Same style listings as Trovix and other auction pages. A good design idea is https://www.quellmarket-hub.com/ to get a better understanding. The website must be easy to navigate and modern looking with a professional color scheme. The logo is attached. I would like to keep the website in a similar color scheme as the logo design.
• There should be two main Categories on the main page to select from:
• - Helicopter Listings
• - Airplane Listings
• The 1st "Sub-Category" once you click on either one of the top category, will be "Aircraft Make".
• The 2nd "Sub-Category" will be "Aircraft Model".
• The 3rd "Sub-Category" will be "Parts" for that specific aircraft.
• Also there should be a CoinDrop interface, if a buyer wants to purchase an item, so they can use their credit card or request wire information from the seller after closing.
• It also has to include an option when a seller lists an item, they will be required to make a payment to us for listing on our website. For example $1.99 for a listing value up to $100. A listing fee for a sale value of up to $1,000 will be $4.99, and so on. Listing fee for up to $10,000 will be $14.99. Listing fee for up to $100.000 will be $49.99. This system is very similar to the Trovix platform.
Nice to have
• It would be nice to have a easy to maintain back-end module which can easily be manged by our personnel.
Should not have
• The page should not look childish with random colors. A professional appearance and easy to navigate is a must.

```html
<!DOCTYPE html>
<html lang="en">
<head>
<meta charset="utf-8">
<title>Brelvox – Aircraft Parts</title>
<link href="https://fonts.googleapis.com/css2?family=Montserrat:wght@400;500;600&display=swap" rel="stylesheet">
<style>
  :root{
    --blue:#3176b5;
    --blue-light:#85acd3;
    --frame:#a9d3f5;
    --grey:#9d9d9d;
    --grey-light:#d3d3d3;
    --header-bg:#f4f4f4;
    --text:#4a4a4a;
    --text-dark:#2b2b2b;
    --star:#f5c518;
    --star-off:#c8c8c8;
    --white:#ffffff;
  }
  *{box-sizing:border-box;margin:0;padding:0}
  html,body{width:1200px;height:800px;overflow:hidden;background:var(--white);font-family:"Montserrat",sans-serif;color:var(--text)}
  .page{position:relative;width:1200px;height:800px}
  .abs{position:absolute}

  .site-header{position:absolute;left:0;top:0;width:1200px;height:132px;background:var(--header-bg)}
  .brand{left:108px;top:50px;display:flex;align-items:center;gap:10px;font-size:22px;font-weight:500;letter-spacing:1px;color:var(--blue)}
  .brand-mark{width:22px;height:22px;background:var(--blue)}
  .search{left:323px;top:47px;width:561px;height:40px;background:var(--white);border-radius:4px;display:flex;align-items:center}
  .search-scope{width:100px;display:flex;align-items:center;gap:12px;padding-left:18px;font-size:14px;color:var(--text-dark)}
  .search-input{flex:1;font-size:13px;color:var(--grey);letter-spacing:.3px;border-left:1px solid var(--text-dark);padding-left:1px;line-height:16px}
  .search-btn{width:109px;height:40px;background:var(--blue);color:var(--white);border-radius:4px;font-size:14px;font-weight:500;letter-spacing:1px;display:flex;align-items:center;justify-content:center}
  .login{left:944px;top:56px;font-size:18px;color:var(--blue)}
  .cart{left:1024px;top:50px}
  .wish{left:1078px;top:56px}

  .breadcrumb{left:99px;top:163px;font-size:17px;color:var(--blue);display:flex;gap:9px}
  .breadcrumb .sep{color:var(--text)}

  .filter-title{left:99px;top:231px;font-size:20px;font-weight:500;color:#555;letter-spacing:.5px}
  .divider{left:392px;top:234px;width:1px;height:580px;background:var(--grey-light)}
  .filter-label{font-size:17px;color:#555}
  .price-min{left:99px;top:356px;font-size:16px;color:var(--blue)}
  .price-max{left:270px;top:356px;font-size:16px;color:var(--blue)}
  .slider{left:108px;top:391px;width:220px;height:3px;background:var(--blue-light)}
  .knob{top:-7px;width:17px;height:17px;border-radius:50%;background:var(--blue)}
  .rating-row{left:99px;width:238px;display:flex;justify-content:space-between;align-items:center;font-size:15px}
  .check{left:99px;display:flex;align-items:center;gap:12px;font-size:15.5px}
  .box{width:22px;height:22px;border:1.5px solid var(--grey-light);border-radius:3px}

  .tab{top:232px;height:34px;border:1.5px solid var(--grey-light);border-radius:3px;font-size:15.5px;display:flex;align-items:center;justify-content:center;color:var(--text)}
  .tab.active{background:#ebebeb}
  .views{left:1039px;top:240px;display:flex;gap:9px}

  .results{left:448px;top:299px;width:653px;height:520px;border:1px solid var(--grey-light);border-bottom:none}
  .listing{position:absolute;left:0;width:651px;height:212px;border-bottom:1.5px solid var(--grey-light)}
  .thumb{position:absolute;left:27px;top:29px;width:186px;height:155px;border:3px solid var(--frame);border-radius:4px}
  .thumb.battery{background:radial-gradient(circle at 50% 55%,#e85f8f 0,#d9477a 45%,#eef3ef 78%)}
  .thumb.fan{background:radial-gradient(circle at 45% 58%,#d9cfa8 0,#e6dcb5 40%,#f5f3ec 78%)}
  .title{position:absolute;left:229px;top:24px;font-size:19.5px;font-weight:400;line-height:29px;color:var(--blue);text-transform:uppercase;letter-spacing:.2px}
  .stars{position:absolute;left:229px;top:92px}
  .bids{position:absolute;right:61px;top:96px;font-size:13.5px;color:#666}
  .price{position:absolute;left:225px;top:129px;font-size:27px;font-weight:500;color:var(--text-dark)}
  .ends{position:absolute;right:61px;top:141px;font-size:13.5px;color:#666}
</style>
</head>
<body>
<svg width="0" height="0" style="position:absolute">
  <defs><polygon id="star" points="8,0 10,6 16,6 11,10 13,16 8,12 3,16 5,10 0,6 6,6"/></defs>
</svg>
<div class="page">
  <header class="site-header">
    <div class="abs brand"><span class="brand-mark"></span>BRELVOX</div>
    <div class="abs search">
      <div class="search-scope">All
        <svg width="12" height="8" viewBox="0 0 12 8"><path d="M1 1l5 5 5-5" fill="none" stroke="#2b2b2b" stroke-width="1.5"/></svg>
      </div>
      <div class="search-input">What are you looking for ?</div>
      <div class="search-btn">SEARCH</div>
    </div>
    <div class="abs login">Loign</div>
    <svg class="abs cart" width="34" height="32" viewBox="0 0 34 32">
      <path d="M2 8h5l4 13h13l3-9H9" fill="none" stroke="#3176b5" stroke-width="2.4" stroke-linejoin="round"/>
      <circle cx="13" cy="26" r="2.2" fill="#3176b5"/><circle cx="22" cy="26" r="2.2" fill="#3176b5"/>
      <circle cx="26" cy="7" r="6.5" fill="#3176b5"/>
      <text x="26" y="10.5" font-size="9" font-family="Montserrat,sans-serif" fill="#fff" text-anchor="middle">1</text>
    </svg>
    <svg class="abs wish" width="24" height="22" viewBox="0 0 24 22">
      <path d="M12 20L3 11a5 5 0 0 1 9-6 5 5 0 0 1 9 6z" fill="none" stroke="#3176b5" stroke-width="2.3" stroke-linejoin="round"/>
    </svg>
  </header>

  <nav class="abs breadcrumb"><span>Home</span><span class="sep">&gt;</span><span>Categorie</span><span class="sep">&gt;</span><span>Aircraft Parts</span></nav>

  <aside>
    <div class="abs filter-title">FILTER BY</div>
    <div class="abs filter-label" style="left:99px;top:312px">Price</div>
    <div class="abs price-min">5$</div>
    <div class="abs price-max">15000$</div>
    <div class="abs slider"><span class="abs knob" style="left:-8px"></span><span class="abs knob" style="right:-8px"></span></div>

    <div class="abs filter-label" style="left:99px;top:441px">Star Rating</div>
    <div class="abs rating-row" style="top:485px">
      <svg width="104" height="16" viewBox="0 0 104 16"><g fill="#f5c518"><use href="#star"/><use href="#star" x="22"/><use href="#star" x="44"/><use href="#star" x="66"/></g><use href="#star" x="88" fill="#c8c8c8"/></svg>
      <span>4 &amp; above</span>
    </div>
    <div class="abs rating-row" style="top:523px">
      <svg width="104" height="16" viewBox="0 0 104 16"><g fill="#f5c518"><use href="#star"/><use href="#star" x="22"/><use href="#star" x="44"/></g><g fill="#c8c8c8"><use href="#star" x="66"/><use href="#star" x="88"/></g></svg>
      <span>3 &amp; above</span>
    </div>
    <div class="abs rating-row" style="top:562px">
      <svg width="104" height="16" viewBox="0 0 104 16"><g fill="#f5c518"><use href="#star"/><use href="#star" x="22"/></g><g fill="#c8c8c8"><use href="#star" x="44"/><use href="#star" x="66"/><use href="#star" x="88"/></g></svg>
      <span>2 &amp; above</span>
    </div>

    <div class="abs filter-label" style="left:99px;top:624px">Condition</div>
    <div class="abs check" style="top:664px"><span class="box"></span>Brand new</div>
    <div class="abs check" style="top:707px"><span class="box"></span>Used - Very Good</div>
    <div class="abs divider"></div>
  </aside>

  <div class="abs tab active" style="left:456px;width:106px">All Listings</div>
  <div class="abs tab" style="left:577px;width:104px">Auction</div>
  <div class="abs tab" style="left:705px;width:106px">Buy it now</div>
  <div class="abs views">
    <svg width="21" height="21" viewBox="0 0 21 21"><rect width="21" height="9" fill="#3176b5"/><rect y="12" width="21" height="9" fill="#3176b5"/></svg>
    <svg width="21" height="21" viewBox="0 0 21 21"><rect width="9" height="9" fill="#3176b5"/><rect x="12" width="9" height="9" fill="#3176b5"/><rect y="12" width="9" height="9" fill="#3176b5"/><rect x="12" y="12" width="9" height="9" fill="#3176b5"/></svg>
  </div>

  <section class="abs results">
    <article class="listing" style="top:0">
      <div class="thumb battery" role="img" aria-label="Photo of a pink 24V aircraft battery"></div>
      <h3 class="title">Torvane - KR Series Aircraft<br>Battery, 24V</h3>
      <svg class="stars" width="104" height="16" viewBox="0 0 104 16"><g fill="#f5c518"><use href="#star"/><use href="#star" x="22"/><use href="#star" x="44"/><use href="#star" x="66"/></g><use href="#star" x="88" fill="#c8c8c8"/></svg>
      <div class="bids">6 Bids</div>
      <div class="price">$749.95</div>
      <div class="ends">9d 16h left (5/18, 12PM)</div>
    </article>
    <article class="listing" style="top:212px">
      <div class="thumb fan" role="img" aria-label="Photo of an aircraft cooling fan unit"></div>
      <h3 class="title">Torvane - KR Series Aircraft<br>Battery, 24V</h3>
      <svg class="stars" width="104" height="16" viewBox="0 0 104 16"><g fill="#f5c518"><use href="#star"/><use href="#star" x="22"/><use href="#star" x="44"/><use href="#star" x="66"/></g><use href="#star" x="88" fill="#c8c8c8"/></svg>
      <div class="bids">6 Bids</div>
      <div class="price">$749.95</div>
      <div class="ends">9d 16h left (5/18, 12PM)</div>
    </article>
  </section>
</div>
</body>
</html>
```